Power Point CI

Creat a Slide Master which we can use and also add new slides with bullets, or other graphic design which we can fill. Power Point Master Format - also amend the graphics on the PPT - especially the project roadmap or profile page. have a look on our website www.brightlantern.io. I would also appreciate other slides which we can use and fill

Target Market(s)

companies - PE, HR Executive

Industry/Entity Type

Executive Search

Font styles to use
Serif
Other font styles liked:
• Calibri or Coast like on our website

Colors
0094D4
00A9DD
6FCCEA
C7EBF8
E9F6FB

Requirements
Must have
• needs to sleek and slim - prefer white and bright elegant Backgrounds
Nice to have
• it should somehow fit to our website and corporate CI
Should not have
• Full green CI

```html
<!DOCTYPE html>
<html lang="en">
<head>
<meta charset="utf-8">
<title>Bright Lantern – Presentation Master</title>
<link rel="stylesheet" href="https://fonts.googleapis.com/css2?family=Roboto+Condensed:wght@300;400;700&family=Roboto:wght@300;400;700&display=swap">
<style>
:root{
  --blue:#0094d4;--sky:#00a9dd;--light:#6fccea;--pale:#c7ebf8;--mist:#e9f6fb;
  --deep:#0a6f9e;--navy:#0b3f52;--title:#0b4a63;--ink:#333c44;--grey:#8a9299;
  --canvas:#dcdcdf;--accent:#e8402f;
}
*{box-sizing:border-box;margin:0;padding:0}
html,body{width:1200px;height:3419px;overflow:hidden}
body{background:var(--canvas);font-family:"Roboto",Arial,sans-serif;color:var(--ink);position:relative}
.cond{font-family:"Roboto Condensed","Arial Narrow",sans-serif}
.slide{position:absolute;width:540px;height:304px;overflow:hidden;background:#fff}
.abs{position:absolute}
.blue-bg{background:linear-gradient(125deg,#2ea3c9 0%,#178db9 45%,#0a72a2 100%)}
.artwork{position:absolute;background:radial-gradient(ellipse at 45% 45%,rgba(233,246,251,.32),rgba(199,235,248,.12) 60%,rgba(199,235,248,0) 100%)}
.artwork.on-white{background:radial-gradient(ellipse at 45% 45%,rgba(199,235,248,.75),rgba(233,246,251,.4) 60%,rgba(255,255,255,0) 100%)}
.cities{position:absolute;left:0;right:0;bottom:0;height:32px;display:flex;align-items:center;justify-content:center;font:500 6.5px "Roboto Condensed",sans-serif;letter-spacing:1.3px;color:var(--title);background:#fff}
.cities.dark{background:var(--navy);color:#fff}
.cover-title{font:700 26px/29px "Roboto Condensed",sans-serif;color:#fff}
.cover-text{font-size:6.2px;line-height:8px;color:#fff}
.wordmark{font:300 19px "Roboto Condensed",sans-serif;letter-spacing:4px;color:#fff;text-transform:uppercase}
.slide-title{position:absolute;left:0;right:0;top:22px;text-align:center;font:400 14.5px "Roboto Condensed",sans-serif;color:var(--title)}
.footer{position:absolute;left:13px;right:15px;top:278px;height:10px;border-radius:5px;background:linear-gradient(90deg,var(--light),var(--sky) 60%,var(--blue));display:flex;justify-content:flex-end;align-items:center;gap:12px;padding-right:8px;font:700 4px "Roboto",sans-serif;color:#fff}
.footer-brand{position:absolute;left:20px;top:266px;font:700 5.5px "Roboto Condensed",sans-serif;color:var(--blue);letter-spacing:.5px}
.photo{position:absolute;background:linear-gradient(160deg,#9a9a9a,#4a4a4a 60%,#222)}
.round{border-radius:50%}
.member{position:absolute;top:52px;width:130px;text-align:center}
.member .photo{position:relative;width:90px;height:90px;margin:0 auto}
.member h3{height:18px;margin-top:22px;display:flex;align-items:center;justify-content:center;font:700 7px/8px "Roboto Condensed",sans-serif;color:var(--title);text-transform:uppercase}
.member p{margin-top:8px;font-size:4.6px;line-height:5.6px;color:var(--grey)}
.bio-name{position:absolute;left:30px;top:30px;font:300 17px/20px "Roboto Condensed",sans-serif;color:var(--title)}
.bio-text{position:absolute;left:30px;top:100px;width:255px;font-size:5px;line-height:6.2px;color:var(--grey)}
.bio-text p{margin-bottom:5px}
.bullets{position:absolute;top:100px;width:215px;font-size:6px;line-height:7.4px;color:var(--grey);list-style:none}
.bullets li{position:relative;padding-left:9px;margin-bottom:8px}
.bullets li::before{content:"";position:absolute;left:0;top:2.5px;width:3px;height:3px;border-radius:50%;background:var(--blue)}
.bullets b{color:var(--title)}
.value{position:absolute;top:82px;width:110px;text-align:center}
.value .icon{width:32px;height:32px;margin:0 auto;border-radius:50%;background:var(--blue);display:flex;align-items:center;justify-content:center}
.value h4{margin-top:10px;font:400 7px "Roboto Condensed",sans-serif;color:var(--title)}
.value p{margin-top:6px;font-size:4.3px;line-height:5.3px;color:var(--grey)}
.ref{position:absolute;top:88px;width:232px}
.ref h4{font:400 7px "Roboto Condensed",sans-serif;color:var(--blue);margin-bottom:8px}
.ref .row{display:flex;height:23px;align-items:center;font-size:5px;padding-left:4px}
.ref .row:nth-child(even){background:#f2f3f4}
.ref .row:nth-child(odd){background:#e3e5e7}
.ref .row b{width:115px;color:var(--navy)}
.phase-label{position:absolute;top:64px;font:700 5.5px "Roboto Condensed",sans-serif;color:var(--title)}
.step{position:absolute;width:90px;text-align:center;margin-left:-45px}
.step .icon{width:28px;height:28px;margin:0 auto;border-radius:50%;background:var(--blue);display:flex;align-items:center;justify-content:center}
.step h4{margin-top:6px;font:400 6.5px "Roboto Condensed",sans-serif;color:var(--title)}
.step p{margin-top:3px;font-size:4.2px;line-height:5px;color:var(--grey)}
.gantt-bar{position:absolute;height:5px;border-radius:3px;background:linear-gradient(90deg,var(--light),var(--blue))}
.gantt-note{position:absolute;font-size:3.8px;color:var(--grey)}
.gantt-dot{position:absolute;width:9px;height:9px;border-radius:2px;background:var(--blue)}
.tool-item{position:absolute;left:313px;display:flex;align-items:center;gap:10px;font-size:5.5px;line-height:6.5px;color:var(--grey)}
.tool-item .icon{width:20px;height:20px;border-radius:50%;background:var(--mist);border:1px solid var(--pale);display:flex;align-items:center;justify-content:center;flex:none}
.contact{position:absolute;left:282px;display:flex;align-items:center;gap:7px;font-size:6px;color:#fff}
.hero{position:absolute;left:162px;top:86px;width:876px;height:493px;overflow:hidden}
.hero .slide{transform:scale(1.6222);transform-origin:0 0}
</style>
</head>
<body>

<div class="hero">
  <section class="slide cover blue-bg">
    <div class="artwork" style="left:15px;top:8px;width:250px;height:262px" role="img" aria-label="Area for the pale origami bird illustration"></div>
    <h1 class="cover-title abs" style="left:267px;top:104px">Presentation Title<br>Goes Here!</h1>
    <p class="cover-text abs" style="left:267px;top:176px;width:230px">Lorem ipsum dolor sit amet, consectetur adipiscing elit. Vivamus eu dui ex. Curabitur dapibus dignissim dui, in molestie metus feugiat sed.</p>
    <p class="cover-text abs" style="left:267px;top:222px;font-size:4.8px">Monday, April 24, 2023</p>
    <div class="cities">Hamburg | Wien | Berlin | München</div>
  </section>
</div>

<section class="slide cover blue-bg" style="left:52px;top:808px">
  <div class="artwork" style="left:15px;top:8px;width:250px;height:262px" role="img" aria-label="Area for the pale origami bird illustration"></div>
  <h1 class="cover-title abs" style="left:267px;top:104px">Presentation Title<br>Goes Here!</h1>
  <p class="cover-text abs" style="left:267px;top:176px;width:230px">Lorem ipsum dolor sit amet, consectetur adipiscing elit. Vivamus eu dui ex. Curabitur dapibus dignissim dui, in molestie metus feugiat sed.</p>
  <p class="cover-text abs" style="left:267px;top:222px;font-size:4.8px">Monday, April 24, 2023</p>
  <div class="cities">Hamburg | Wien | Berlin | München</div>
</section>

<section class="slide cover" style="left:609px;top:808px">
  <div class="artwork on-white" style="left:15px;top:8px;width:250px;height:262px" role="img" aria-label="Area for the light blue origami bird illustration"></div>
  <h1 class="cover-title abs" style="left:267px;top:104px;color:var(--title)">Presentation Title<br>Goes Here!</h1>
  <p class="cover-text abs" style="left:267px;top:176px;width:230px;color:var(--grey)">Lorem ipsum dolor sit amet, consectetur adipiscing elit. Vivamus eu dui ex. Curabitur dapibus dignissim dui, in molestie metus feugiat sed.</p>
  <p class="cover-text abs" style="left:267px;top:222px;font-size:4.8px;color:var(--grey)">Monday, April 24, 2023</p>
  <div class="cities dark">Hamburg | Wien | Berlin | München</div>
</section>

<section class="slide chapter blue-bg" style="left:52px;top:1131px">
  <div class="wordmark abs" style="left:0;right:0;top:155px;text-align:center">Bright Lantern</div>
  <div class="cities">Hamburg | Wien | Berlin | München</div>
</section>

<section class="slide chapter blue-bg" style="left:609px;top:1131px">
  <div class="wordmark abs" style="left:42px;top:68px;font-size:10px;letter-spacing:2px">Bright Lantern</div>
  <h1 class="cover-title abs" style="left:42px;top:110px;font-size:23px;line-height:27px">Presentation Title Goes<br>Here!</h1>
  <p class="cover-text abs" style="left:42px;top:175px;width:300px">Lorem ipsum dolor sit amet, consectetur adipiscing elit. Vivamus eu dui ex. Curabitur dapibus dignissim dui, in molestie metus feugiat sed. Praesent aliquet lorem ex, eu dapibus odio varius at.</p>
  <div class="abs" style="left:42px;top:215px;width:97px;height:20px;border:1px solid #fff;border-radius:3px;color:#fff;font:700 4.8px 'Roboto',sans-serif;display:flex;align-items:center;justify-content:center">Monday, April 24, 2023</div>
  <div class="cities">Hamburg | Wien | Berlin | München</div>
</section>

<section class="slide team" style="left:52px;top:1452px">
  <h2 class="slide-title">Unser Team. Für Ihr Team.</h2>
  <div class="member" style="left:45px"><div class="photo round" role="img" aria-label="Portrait photo of team member"></div><h3>Dr. Med Clara Vollmer-<br>Stein</h3><p>Lorem ipsum dolor sit amet, consectetur adipiscing elit. Vivamus eu dui ex. Curabitur dapibus dignissim dui, in molestie metus feugiat sed. Praesent aliquet lorem ex, eu dapibus odio varius at, consequat lacus vitae.</p></div>
  <div class="member" style="left:205px"><div class="photo round" role="img" aria-label="Portrait photo of team member"></div><h3>Lena Hartwig</h3><p>Lorem ipsum dolor sit amet, consectetur adipiscing elit. Vivamus eu dui ex. Curabitur dapibus dignissim dui, in molestie metus feugiat sed. Praesent aliquet lorem ex, eu dapibus odio varius at, consequat lacus vitae.</p></div>
  <div class="member" style="left:363px"><div class="photo round" role="img" aria-label="Portrait photo of team member"></div><h3 style="text-transform:none">Jonas Rieder</h3><p>Lorem ipsum dolor sit amet, consectetur adipiscing elit. Vivamus eu dui ex. Curabitur dapibus dignissim dui, in molestie metus feugiat sed. Praesent aliquet lorem ex, eu dapibus odio varius at, consequat lacus vitae.</p></div>
  <div class="footer-brand">Bright Lantern</div>
  <div class="footer"><span>https://www.brightlantern.io</span><span>5</span></div>
</section>

<section class="slide team" style="left:609px;top:1452px">
  <h2 class="slide-title">Unser Team. Für Ihr Team.</h2>
  <div class="member" style="left:45px"><div class="photo round" role="img" aria-label="Portrait photo of team member"></div><h3 style="text-transform:none">Petra Lindner</h3><p>Lorem ipsum dolor sit amet, consectetur adipiscing elit. Vivamus eu dui ex. Curabitur dapibus dignissim dui, in molestie metus feugiat sed. Praesent aliquet lorem ex, eu dapibus odio varius at, consequat lacus vitae.</p></div>
  <div class="member" style="left:205px"><div class="photo round" role="img" aria-label="Portrait photo of team member"></div><h3 style="text-transform:none">Miriam Kessler</h3><p>Lorem ipsum dolor sit amet, consectetur adipiscing elit. Vivamus eu dui ex. Curabitur dapibus dignissim dui, in molestie metus feugiat sed. Praesent aliquet lorem ex, eu dapibus odio varius at, consequat lacus vitae.</p></div>
  <div class="member" style="left:363px"><div class="photo round" role="img" aria-label="Portrait photo of team member"></div><h3 style="text-transform:none">Defne Aksoy</h3><p>Lorem ipsum dolor sit amet, consectetur adipiscing elit. Vivamus eu dui ex. Curabitur dapibus dignissim dui, in molestie metus feugiat sed. Praesent aliquet lorem ex, eu dapibus odio varius at, consequat lacus vitae.</p></div>
  <div class="footer-brand">Bright Lantern</div>
  <div class="footer"><span>https://www.brightlantern.io</span><span>6</span></div>
</section>

<section class="slide profile" style="left:52px;top:1774px">
  <h2 class="bio-name">Dr. Clara<br>Vollmer-Stein</h2>
  <div class="bio-text">
    <p>Clara knows what modern leadership is all about, and that from many points of view – she has guided many leaders into new roles and has held senior positions herself for several years.</p>
    <p>As a graduate of medicine she first worked in a university hospital, then moved into strategy consulting and built a leadership academy for healthcare. She later co-founded a digital health start-up and served as chief people officer of a fast-growing scale-up before she joined Bright Lantern in 2021, bringing this broad experience to every search.</p>
    <p>Clara lives in Hamburg with her family.</p>
  </div>
  <div class="photo" style="left:303px;top:0;width:211px;height:252px" role="img" aria-label="Black and white portrait photo"></div>
  <div class="footer-brand">Bright Lantern</div>
  <div class="footer"><span>https://www.brightlantern.io</span><span>7</span></div>
</section>

<section class="slide profile" style="left:609px;top:1774px">
  <h2 class="bio-name">Lena Hartwig</h2>
  <div class="bio-text" style="top:98px">
    <p>Lena started her career as a global product manager in industry before she spent three years in London as a sales manager for an international airline.</p>
    <p>She then accepted an offer from an executive search firm where she learned the skills of research.</p>
    <p>When her partner was transferred abroad, she became self-employed and worked for several search partners; now back in Vienna, she founded a chapter together with Clara.</p>
    <p>Lena studied international business in Vienna and graduated from a master programme. She is mother of two children.</p>
  </div>
  <div class="photo" style="left:304px;top:0;width:210px;height:252px" role="img" aria-label="Black and white portrait photo"></div>
  <div class="footer-brand">Bright Lantern</div>
  <div class="footer"><span>https://www.brightlantern.io</span><span>8</span></div>
</section>

<section class="slide about" style="left:52px;top:2096px">
  <h2 class="slide-title">Who We Are and How We Work</h2>
  <ul class="bullets" style="left:30px">
    <li><b>Longstanding experience</b> with a passion for placing (C-Level) Executives in Healthcare and other industries</li>
    <li>In-depth expertise strong networks in healthcare and, covering all <b>relevant sub-sectors</b> (HC Services, PE Healthcare Rollups, Elderly Care Chains, Physiotherapy, Digital Health, Medical Technology, Healthcare IT), including relevant expertise regarding the regulatory environment in Germany</li>
    <li>Expertise beyond placement and HR topics, allowing for eye-level discussion around your business</li>
  </ul>
  <ul class="bullets" style="left:290px">
    <li><b>Creative approaches</b> to finding – and convincing – candidates</li>
    <li><b>Structured</b> and lean <b>digital search processes</b>, high transparency, comprehensive candidate evaluation</li>
    <li><b>Referencing</b> of candidates as part of the search process; psychometrics on demand</li>
    <li>Onboarding support to ensure a good start for the candidate</li>
    <li>We work with you <b>personally</b> and act as an <b>ambassador</b> for our clients in the market</li>
  </ul>
  <div class="footer-brand">Bright Lantern</div>
  <div class="footer"><span>https://www.brightlantern.io</span><span>9</span></div>
</section>

<section class="slide values" style="left:609px;top:2096px">
  <h2 class="slide-title">Our Values</h2>
  <div class="abs" style="left:0;right:0;top:98px;border-top:1px dashed var(--light)"></div>
  <div class="value" style="left:29px"><div class="icon"><svg width="16" height="16" viewBox="0 0 16 16"><path d="M8 14 2.5 8.5A3.3 3.3 0 0 1 8 4a3.3 3.3 0 0 1 5.5 4.5Z" fill="none" stroke="#fff" stroke-width="1.4"/></svg></div><h4>HONEST</h4><p>We only work with clients who can benefit from our expertise. We are not interested in status symbols, only in achieving results in a way that is transparent and beneficial for everyone.</p></div>
  <div class="value" style="left:152px"><div class="icon"><svg width="16" height="16" viewBox="0 0 16 16"><circle cx="8" cy="5.5" r="3" fill="#fff"/><path d="M2.5 14a5.5 5.5 0 0 1 11 0Z" fill="#fff"/></svg></div><h4>PERSONAL</h4><p>We put all of our resources into finding you the top talents you are looking for – and we get involved ourselves. We have excellent networks and we are always hot on the heels of fresh talent. That is how we find the people that you need right now.</p></div>
  <div class="value" style="left:275px"><div class="icon"><svg width="16" height="16" viewBox="0 0 16 16"><circle cx="8" cy="8" r="5.5" fill="none" stroke="#fff" stroke-width="1.4"/><path d="M8 2.5v11M2.5 8h11" stroke="#fff" stroke-width="1.2"/></svg></div><h4>PRAGMATIC</h4><p>We work fast. But we don't start until we have a clear goal. We begin by asking: how will you know the appointment was successful three years from now? This thought drives our process – streamlined, digital and constantly in communication with you.</p></div>
  <div class="value" style="left:398px"><div class="icon"><svg width="16" height="16" viewBox="0 0 16 16"><circle cx="5" cy="6" r="2.2" fill="#fff"/><circle cx="11" cy="6" r="2.2" fill="#fff"/><path d="M1 13a4 4 0 0 1 8 0ZM7 13a4 4 0 0 1 8 0Z" fill="#fff"/></svg></div><h4>DIVERSE</h4><p>We know where the obstacles lie, and we know where things get tough – we have worked through them ourselves, as employees, managers and founders. That's how we know how diversity really works, and how your company can best benefit.</p></div>
  <div class="footer-brand">Bright Lantern</div>
  <div class="footer"><span>https://www.brightlantern.io</span><span>10</span></div>
</section>

<section class="slide references" style="left:52px;top:2417px">
  <h2 class="slide-title">Relevant reference assignments (excerpt)</h2>
  <div class="ref" style="left:25px"><h4>POSITION TO BE DEFINED</h4>
    <div class="row"><b>Explanation</b>Investor/Owner</div><div class="row"><b>Explanation</b>Investor/Owner</div><div class="row"><b>Explanation</b>Investor/Owner</div><div class="row"><b>Explanation</b>Investor/Owner</div><div class="row"><b>Explanation</b>Investor/Owner</div>
  </div>
  <div class="ref" style="left:280px"><h4>POSITION TO BE DEFINED</h4>
    <div class="row"><b>Explanation</b>Investor/Owner</div><div class="row"><b>Explanation</b>Investor/Owner</div><div class="row"><b>Explanation</b>Investor/Owner</div><div class="row"><b>Explanation</b>Investor/Owner</div><div class="row"><b>Explanation</b>Investor/Owner</div>
  </div>
  <div class="footer-brand">Bright Lantern</div>
  <div class="footer"><span>https://www.brightlantern.io</span><span>11</span></div>
</section>

<section class="slide section-break blue-bg" style="left:609px;top:2417px">
  <div class="artwork" style="left:15px;top:0;width:260px;height:300px" role="img" aria-label="Area for the pale origami bird illustration"></div>
  <h1 class="abs" style="left:268px;top:150px;font:300 23px 'Roboto Condensed',sans-serif;color:#fff">Section Break</h1>
  <p class="cover-text abs" style="left:268px;top:184px;width:230px">Lorem ipsum dolor sit amet, consectetur adipiscing elit. Vivamus eu dui ex. Curabitur dapibus dignissim dui, in molestie metus feugiat sed.</p>
</section>

<section class="slide process" style="left:52px;top:2740px">
  <h2 class="slide-title">Search Process</h2>
  <span class="phase-label" style="left:100px">Phase 1</span>
  <span class="phase-label" style="left:265px">Phase 2</span>
  <span class="phase-label" style="left:430px">Phase 3</span>
  <div class="abs" style="left:0;right:0;top:74px;height:17px;background:var(--blue);display:flex;color:#fff;font:400 5px 'Roboto Condensed',sans-serif">
    <span style="flex:1;text-align:center;line-height:17px">Research - Longlist</span>
    <svg width="10" height="17" viewBox="0 0 10 17"><path d="M2 1l6 7.5L2 16" fill="none" stroke="#6fccea" stroke-width="2"/></svg>
    <span style="flex:1;text-align:center;line-height:17px">Focus &amp; Interviews - Shortlist</span>
    <svg width="10" height="17" viewBox="0 0 10 17"><path d="M2 1l6 7.5L2 16" fill="none" stroke="#6fccea" stroke-width="2"/></svg>
    <span style="flex:1;text-align:center;line-height:17px">Completion</span>
  </div>
  <div class="abs" style="left:0;right:0;top:107px;border-top:1px dashed var(--light)"></div>
  <span class="abs" style="left:22px;top:112px;font-size:4.5px;color:var(--title)">CW 1</span>
  <span class="abs" style="left:506px;top:112px;font-size:4.5px;color:var(--title)">CW 2</span>
  <svg class="abs" style="left:0;top:100px" width="540" height="80">
    <g stroke="#9bd6ee" stroke-width=".7"><line x1="58" y1="7" x2="58" y2="37"/><line x1="163" y1="7" x2="163" y2="70"/><line x1="268" y1="7" x2="268" y2="37"/><line x1="374" y1="7" x2="374" y2="70"/><line x1="479" y1="7" x2="479" y2="37"/></g>
    <g fill="#0094d4"><circle cx="58" cy="7" r="3"/><circle cx="163" cy="7" r="3"/><circle cx="268" cy="7" r="3"/><circle cx="374" cy="7" r="3"/><circle cx="479" cy="7" r="3"/></g>
  </svg>
  <div class="step" style="left:58px;top:137px"><div class="icon"><svg width="12" height="14" viewBox="0 0 12 14"><rect x="1" y="1" width="10" height="12" rx="1.5" fill="#fff"/></svg></div><h4>Kickoff</h4><p>Discuss and agree on profile, position specification and target list</p></div>
  <div class="step" style="left:163px;top:170px"><div class="icon"><svg width="14" height="14" viewBox="0 0 14 14"><circle cx="6" cy="6" r="4" fill="none" stroke="#fff" stroke-width="1.6"/><path d="M9 9l4 4" stroke="#fff" stroke-width="1.8"/></svg></div><h4>Research</h4><p>Active and passive research, approach of potential candidates</p></div>
  <div class="step" style="left:268px;top:137px"><div class="icon"><svg width="16" height="14" viewBox="0 0 16 14"><circle cx="5" cy="4" r="2.3" fill="#fff"/><circle cx="11" cy="4" r="2.3" fill="#fff"/><path d="M1 13a4 4 0 0 1 8 0ZM7 13a4 4 0 0 1 8 0Z" fill="#fff"/></svg></div><h4>Interviews</h4><p>Presentation of shortlisted profiles, client interviews</p></div>
  <div class="step" style="left:374px;top:170px"><div class="icon"><svg width="16" height="14" viewBox="0 0 16 14"><circle cx="8" cy="4" r="2.5" fill="#fff"/><circle cx="3" cy="6" r="1.8" fill="#fff"/><circle cx="13" cy="6" r="1.8" fill="#fff"/><path d="M3 13a5 5 0 0 1 10 0Z" fill="#fff"/></svg></div><h4>References</h4><p>Assessments (optional), taking references</p></div>
  <div class="step" style="left:479px;top:137px"><div class="icon"><svg width="12" height="14" viewBox="0 0 12 14"><path d="M6 1a5 5 0 0 1 5 5v7H1V6a5 5 0 0 1 5-5Z" fill="#fff"/></svg></div><h4>Selection final candidate</h4><p>Contract negotiation and onboarding, feedback discussion</p></div>
  <div class="footer-brand">Bright Lantern</div>
  <div class="footer"><span>https://www.brightlantern.io</span><span>13</span></div>
</section>

<section class="slide timeline" style="left:609px;top:2740px">
  <h2 class="slide-title">Draft Project Timeline for placement</h2>
  <span class="phase-label" style="left:58px;font-size:4.5px;top:62px">Phase 1: Open the search &amp; screen: LONGLIST</span>
  <span class="phase-label" style="left:242px;font-size:4.5px;top:62px">Phase 2: Narrow the focus - SHORTLIST</span>
  <span class="phase-label" style="left:412px;font-size:4.5px;top:62px">Phase 3: Close the search</span>
  <div class="abs" style="left:30px;right:20px;top:72px;border-top:1px solid var(--pale)"></div>
  <svg class="abs" style="left:0;top:72px" width="540" height="140"><g stroke="#c7ebf8" stroke-width=".6" stroke-dasharray="2 2"><line x1="35" y1="0" x2="35" y2="136"/><line x1="64" y1="0" x2="64" y2="136"/><line x1="93" y1="0" x2="93" y2="136"/><line x1="122" y1="0" x2="122" y2="136"/><line x1="151" y1="0" x2="151" y2="136"/><line x1="180" y1="0" x2="180" y2="136"/><line x1="209" y1="0" x2="209" y2="136"/><line x1="238" y1="0" x2="238" y2="136"/><line x1="267" y1="0" x2="267" y2="136"/><line x1="296" y1="0" x2="296" y2="136"/><line x1="325" y1="0" x2="325" y2="136"/><line x1="354" y1="0" x2="354" y2="136"/><line x1="383" y1="0" x2="383" y2="136"/><line x1="412" y1="0" x2="412" y2="136"/><line x1="441" y1="0" x2="441" y2="136"/><line x1="470" y1="0" x2="470" y2="136"/><line x1="499" y1="0" x2="499" y2="136"/></g></svg>
  <div class="gantt-dot" style="left:112px;top:84px"></div><span class="gantt-note" style="left:126px;top:86px">Approach potential candidates</span>
  <div class="gantt-bar" style="left:112px;top:96px;width:195px"></div>
  <div class="gantt-dot" style="left:90px;top:108px"></div><span class="gantt-note" style="left:104px;top:110px">Source &amp; screen the market</span>
  <div class="gantt-bar" style="left:90px;top:120px;width:160px"></div>
  <div class="gantt-dot" style="left:33px;top:136px"></div><span class="gantt-note" style="left:47px;top:138px">Define the target universe</span>
  <div class="gantt-bar" style="left:33px;top:148px;width:75px"></div>
  <span class="gantt-note" style="left:160px;top:134px">Present candidates &amp; client interviews, first referencing</span>
  <span class="gantt-note" style="left:160px;top:140px;color:var(--accent)">Time to first client interview: 5-6 weeks</span>
  <div class="gantt-bar" style="left:160px;top:148px;width:150px"></div>
  <div class="gantt-dot" style="left:15px;top:159px"></div><span class="gantt-note" style="left:29px;top:160px;width:60px">Kick-Off: agree on competency profile and position specification</span>
  <div class="gantt-dot" style="left:140px;top:159px"></div><span class="gantt-note" style="left:154px;top:161px">Bright Lantern interviews</span>
  <div class="gantt-bar" style="left:140px;top:172px;width:220px"></div>
  <svg class="abs" style="left:385px;top:85px" width="10" height="8" viewBox="0 0 10 8"><path d="M1 4l3 3 5-6" fill="none" stroke="#0094d4" stroke-width="1.4"/></svg><span class="gantt-note" style="left:398px;top:87px">Select the final candidate</span>
  <div class="gantt-bar" style="left:392px;top:97px;width:68px"></div>
  <div class="gantt-dot" style="left:398px;top:110px"></div><span class="gantt-note" style="left:412px;top:110px;width:60px">Negotiate contract &amp; begin onboarding<br><span style="color:var(--accent)">Time to close: 3-4 months</span></span>
  <div class="gantt-bar" style="left:398px;top:125px;width:45px"></div>
  <div class="gantt-dot" style="left:398px;top:136px"></div><span class="gantt-note" style="left:412px;top:136px;width:40px">360 degree referencing</span>
  <div class="gantt-dot" style="left:464px;top:159px"></div><span class="gantt-note" style="left:478px;top:160px;width:40px">Collect feedback from client</span>
  <div class="gantt-bar" style="left:460px;top:172px;width:45px"></div>
  <div class="abs" style="left:15px;right:15px;top:208px;border-top:1px solid var(--title)"></div>
  <div class="abs cond" style="left:15px;right:15px;top:211px;display:flex;justify-content:space-between;font-size:4px;color:var(--title)"><span>W</span><span>12</span><span>13</span><span>14</span><span>15</span><span>16</span><span>17</span><span>18</span><span>19</span><span>20</span><span>21</span><span>22</span><span>23</span><span>24</span><span>25</span><span>26</span><span>27</span><span>W</span></div>
  <div class="gantt-bar" style="left:25px;top:220px;width:120px;height:4px"></div>
  <div class="gantt-bar" style="left:145px;top:220px;width:120px;height:4px"></div>
  <div class="gantt-bar" style="left:265px;top:220px;width:120px;height:4px"></div>
  <div class="gantt-bar" style="left:385px;top:220px;width:120px;height:4px"></div>
  <div class="abs" style="left:25px;right:35px;top:228px;display:flex;justify-content:space-between;font-size:3.8px;color:var(--title)"><span>03/2023</span><span>04/2023</span><span>05/2023</span><span>06/2023</span></div>
  <div class="footer-brand">Bright Lantern</div>
  <div class="footer"><span>https://www.brightlantern.io</span><span>14</span></div>
</section>

<section class="slide tool" style="left:52px;top:3061px">
  <div class="abs" style="left:27px;top:28px;width:265px;height:203px;border-radius:10px;background:#1c1f24;padding:7px">
    <div style="width:100%;height:100%;border-radius:4px;background:linear-gradient(180deg,#f7f9fb,#e9eef2)" role="img" aria-label="Screenshot of the candidate tracking web tool on a tablet"></div>
  </div>
  <h2 class="abs" style="left:313px;top:30px;font:400 17px/20px 'Roboto Condensed',sans-serif;color:var(--title)">Digital Tool for<br>Full Transparency</h2>
  <div class="tool-item" style="top:99px"><span class="icon"><svg width="10" height="10" viewBox="0 0 10 10"><circle cx="5" cy="5" r="4" fill="none" stroke="#0094d4" stroke-width="1"/><path d="M5 2.5V5l2 1" fill="none" stroke="#0094d4" stroke-width="1"/></svg></span><span>Follow the progress of the project<br>24/7 real-time</span></div>
  <div class="tool-item" style="top:131px"><span class="icon"><svg width="10" height="10" viewBox="0 0 10 10"><path d="M1 2h8M1 5h8M1 8h8" stroke="#0094d4" stroke-width="1"/></svg></span><span>Prioritize and evaluate candidates<br>and provide feedback</span></div>
  <div class="tool-item" style="top:163px"><span class="icon"><svg width="10" height="10" viewBox="0 0 10 10"><rect x="2" y="1" width="6" height="8" rx="1" fill="#0094d4"/></svg></span><span>You can view the list of target companies at any<br>time</span></div>
  <div class="tool-item" style="top:195px"><span class="icon"><svg width="10" height="10" viewBox="0 0 10 10"><rect x="2.5" y="1" width="5" height="8" rx="1" fill="none" stroke="#0094d4" stroke-width="1"/></svg></span><span>Access to the relevant information on<br>all candidates at all times</span></div>
  <div class="footer-brand">Bright Lantern</div>
  <div class="footer"><span>https://www.brightlantern.io</span><span>15</span></div>
</section>

<section class="slide thanks blue-bg" style="left:609px;top:3061px">
  <div class="artwork" style="left:15px;top:8px;width:250px;height:262px" role="img" aria-label="Area for the pale origami bird illustration"></div>
  <h1 class="abs" style="left:282px;top:100px;font:700 23px 'Roboto Condensed',sans-serif;color:#fff">Thank you!</h1>
  <p class="abs" style="left:282px;top:163px;font:700 7px 'Roboto Condensed',sans-serif;color:#fff">Contact Us</p>
  <div class="contact" style="top:190px"><svg width="8" height="8" viewBox="0 0 8 8"><path d="M1.5 1h1.5l.7 1.8-1 .7a4 4 0 0 0 1.8 1.8l.7-1 1.8.7V6.5A1 1 0 0 1 6 7.5 5.5 5.5 0 0 1 .5 2 1 1 0 0 1 1.5 1Z" fill="#fff"/></svg>Phone Number Goes Here</div>
  <div class="contact" style="top:206px"><svg width="8" height="8" viewBox="0 0 8 8"><circle cx="4" cy="4" r="3.3" fill="none" stroke="#fff" stroke-width=".8"/><circle cx="4" cy="4" r="1.3" fill="none" stroke="#fff" stroke-width=".8"/></svg>E-Mail Address Goes Here</div>
  <div class="contact" style="top:222px"><svg width="8" height="8" viewBox="0 0 8 8"><circle cx="4" cy="4" r="3.3" fill="none" stroke="#fff" stroke-width=".8"/><path d="M.7 4h6.6M4 .7c2 2 2 4.6 0 6.6M4 .7c-2 2-2 4.6 0 6.6" fill="none" stroke="#fff" stroke-width=".6"/></svg>URL Address Goes Here</div>
  <div class="cities">Hamburg | Wien | Berlin | München</div>
</section>

</body>
</html>
```